b-ryx design for startup inpection service

building and pest inspections what i had in mind was b-ryx in large print with prepurchase in small print directly under it and the small tm (tradmark) .Within the C I would like an eye but I don't want to take away from the C so maybe the eye would be done in a fine line?I would also like the Building and Pest inspections to be prominent and large .Have no idea of colors but do like black orange and silver

Target Market(s)

home buyers and realestate agents

Industry/Entity Type

Building

Contact Information for Business Card

b-ryx prepurchase, Phone 0413926058, fax 02 93514770, email b-ryx@mailnest.com.au ,building and pest inspections

Font styles to use
Sans Serif

Requirements
Must have
• bold color
• simple layout
• bold color
• uncluttered layout
Should not have
• contact details the same size as Building and Pest Inspections

```html
<!DOCTYPE html>
<html lang="en">
<head>
<meta charset="utf-8">
<title>B-RYX Prepurchase – Business Card</title>
<link rel="stylesheet" href="https://fonts.googleapis.com/css2?family=Roboto+Condensed:wght@300;700&display=swap">
<style>
  :root {
    --card-dark: #1d2023;
    --card-dark-soft: #2a2e31;
    --brand-orange: #f2420c;
    --headline-orange: #ee4a1c;
    --panel-white: #ffffff;
    --contact-white: #f1f1f1;
  }
  * { margin: 0; padding: 0; box-sizing: border-box; }
  html, body {
    width: 1200px;
    height: 693px;
    overflow: hidden;
    background: var(--card-dark);
  }
  .business-card {
    position: relative;
    width: 1200px;
    height: 693px;
    overflow: hidden;
    background:
      radial-gradient(ellipse 420px 180px at 30% 20%, rgba(255,255,255,0.05), transparent 70%),
      radial-gradient(ellipse 500px 200px at 75% 85%, rgba(255,255,255,0.045), transparent 70%),
      radial-gradient(ellipse 300px 140px at 90% 15%, rgba(255,255,255,0.04), transparent 70%),
      linear-gradient(160deg, var(--card-dark-soft), var(--card-dark) 60%);
  }
  .service-line {
    position: absolute;
    top: 56px;
    left: 0;
    width: 1200px;
    text-align: center;
    font-family: "Roboto Condensed", sans-serif;
    font-weight: 300;
    font-size: 60px;
    letter-spacing: 0.235em;
    text-indent: 0.235em;
    color: var(--headline-orange);
    line-height: 1;
    white-space: nowrap;
  }
  .brand-panel {
    position: absolute;
    top: 175px;
    left: 0;
    width: 1200px;
    height: 293px;
    background: var(--panel-white);
    display: flex;
    align-items: center;
    justify-content: center;
  }
  .brand-panel-edge {
    position: absolute;
    top: 339px;
    left: 0;
    width: 3px;
    height: 129px;
    background: var(--brand-orange);
  }
  .brand-rule {
    position: absolute;
    top: 468px;
    left: 0;
    width: 1200px;
    height: 17px;
    background: var(--brand-orange);
  }
  .brand-name {
    font-family: "Roboto Condensed", sans-serif;
    font-weight: 700;
    font-size: 100px;
    line-height: 1;
    color: var(--brand-orange);
    letter-spacing: 0.01em;
    white-space: nowrap;
  }
  .contact-list {
    position: absolute;
    top: 520px;
    left: 51px;
    list-style: none;
    font-family: "Roboto Condensed", sans-serif;
    font-weight: 300;
    font-size: 34px;
    line-height: 45px;
    color: var(--contact-white);
    white-space: nowrap;
  }
</style>
</head>
<body>
  <main class="business-card">
    <p class="service-line">building and pest inspections</p>

    <section class="brand-panel">
      <h1 class="brand-name">B-RYX PREPURCHASE</h1>
    </section>
    <div class="brand-panel-edge"></div>
    <div class="brand-rule"></div>

    <ul class="contact-list">
      <li>Phone 0413926058</li>
      <li>fax 02 93514770</li>
      <li>email b-ryx@mailnest.com.au</li>
    </ul>
  </main>
</body>
</html>
```